Design some Business Cards for Varnek Electrical Services Pty Ltd.

Attached is a logo for Varnek Electrical Services Pty Ltd. Also is attached a template I would like to have a similar design/font/Colour scheme.

```html
<!DOCTYPE html>
<html lang="en">
<head>
<meta charset="utf-8">
<title>Varnek Electrical Services – Business Cards</title>
<link href="https://fonts.googleapis.com/css2?family=Source+Sans+3:wght@400;600;700&display=swap" rel="stylesheet">
<style>
  :root {
    --page-bg: #2b2b2d;
    --navy: #1f2c6a;
    --navy-deep: #172257;
    --navy-light: #4a5a95;
    --green: #4cb648;
    --green-light: #7fcf58;
    --white: #ffffff;
    --paper-grey: #d3d4d6;
    --logo-navy: #2b3b86;
  }
  * { margin: 0; padding: 0; box-sizing: border-box; }
  html, body { width: 1200px; height: 936px; overflow: hidden; }
  body {
    background: var(--page-bg);
    font-family: "Source Sans 3", "Myriad Pro", Arial, sans-serif;
    position: relative;
  }
  .card {
    position: absolute;
    left: 255px;
    width: 692px;
    height: 393px;
    border-radius: 27px;
    overflow: hidden;
    box-shadow: 0 6px 18px rgba(0,0,0,0.45);
  }
  .card--front { top: 51px; }
  .card--back { top: 491px; }
  .card__art { position: absolute; inset: 0; width: 100%; height: 100%; }

  .brand {
    position: absolute;
    display: flex;
    align-items: center;
    gap: 10px;
    font-weight: 600;
    letter-spacing: 2.5px;
    line-height: 1.15;
  }
  .brand__dot { width: 14px; height: 14px; border-radius: 50%; flex: none; }
  .brand--front { left: 418px; top: 108px; color: var(--logo-navy); font-size: 19px; }
  .brand--front .brand__dot { background: var(--logo-navy); }
  .brand--back {
    left: 0; right: 0; top: 216px; justify-content: center;
    color: var(--white); font-size: 23px; text-align: center;
  }
  .brand--back .brand__dot { background: var(--white); }
  .brand__name small { display: block; font-size: 0.82em; letter-spacing: 3px; }

  .person { position: absolute; left: 32px; top: 195px; }
  .person__name { color: var(--green); font-size: 30px; font-weight: 700; line-height: 1; }
  .person__role { color: var(--white); font-size: 17px; margin-top: 6px; }

  .contacts { position: absolute; left: 32px; top: 268px; list-style: none; }
  .contacts li {
    display: flex; align-items: center; gap: 9px;
    color: var(--white); font-size: 15px; height: 21px;
  }
  .contacts svg { width: 11px; height: 11px; flex: none; }

  .address {
    position: absolute; left: 448px; top: 284px;
    color: var(--white); font-size: 15px; line-height: 22px; font-style: normal;
  }
  .tagline {
    position: absolute; left: 0; right: 0; top: 341px;
    text-align: center; color: var(--white); font-size: 14px;
  }
</style>
</head>
<body>

<section class="card card--front" aria-label="Business card front">
  <svg class="card__art" viewBox="0 0 692 393" preserveAspectRatio="none" aria-hidden="true">
    <defs>
      <linearGradient id="paperTop" x1="0" y1="0" x2="1" y2="0">
        <stop offset="0" stop-color="#ffffff"/>
        <stop offset="0.55" stop-color="#f4f4f5"/>
        <stop offset="0.62" stop-color="var(--paper-grey)"/>
        <stop offset="1" stop-color="#cfd0d2"/>
      </linearGradient>
      <linearGradient id="navyFront" x1="0" y1="0" x2="1" y2="1">
        <stop offset="0" stop-color="#25357a"/>
        <stop offset="1" stop-color="var(--navy-deep)"/>
      </linearGradient>
      <linearGradient id="greenBand" x1="0" y1="0" x2="1" y2="0">
        <stop offset="0" stop-color="var(--green)"/>
        <stop offset="1" stop-color="var(--green-light)"/>
      </linearGradient>
    </defs>
    <rect width="692" height="393" fill="url(#paperTop)"/>
    <path d="M0 174 C60 162 110 130 170 128 C250 126 300 180 380 185 C470 190 560 178 692 168 L692 393 L0 393 Z" fill="url(#greenBand)"/>
    <path d="M0 184 C60 170 110 140 170 140 C250 140 300 196 380 200 C470 204 560 190 692 174 L692 393 L0 393 Z" fill="var(--white)"/>
    <path d="M0 198 C60 184 110 150 170 150 C250 150 300 206 380 210 C470 214 560 196 692 178 L692 393 L0 393 Z" fill="url(#navyFront)"/>
    <path d="M360 393 L520 0 L560 0 L420 393 Z" fill="var(--navy-light)" opacity="0.35"/>
  </svg>

  <div class="brand brand--front">
    <span class="brand__dot"></span>
    <span class="brand__name">Varnek Electrical<small>Services Pty Ltd</small></span>
  </div>

  <div class="person">
    <p class="person__name">Darren Kell</p>
    <p class="person__role">President</p>
  </div>

  <ul class="contacts">
    <li>
      <svg viewBox="0 0 12 12"><path d="M2.5 1 L4.5 1 L5.2 3.6 L4 4.6 C4.6 6 6 7.4 7.4 8 L8.4 6.8 L11 7.5 L11 9.5 C11 10.3 10.3 11 9.5 11 C5 10.6 1.4 7 1 2.5 C1 1.7 1.7 1 2.5 1 Z" fill="var(--green)"/></svg>
      (000) 987 654 321
    </li>
    <li>
      <svg viewBox="0 0 12 12"><rect x="3" y="1" width="6" height="3" fill="var(--green)"/><rect x="1" y="4.5" width="10" height="4.5" rx="1" fill="var(--green)"/><rect x="3" y="8" width="6" height="3" fill="var(--green)"/></svg>
      darren@varnekelectrical.com.au
    </li>
    <li>
      <svg viewBox="0 0 12 12"><rect x="1" y="2.5" width="10" height="7" fill="none" stroke="var(--green)" stroke-width="1.3"/><path d="M1 2.5 L6 6.5 L11 2.5" fill="none" stroke="var(--green)" stroke-width="1.3"/></svg>
      www.varnekelectrical.com.au
    </li>
    <li>
      <svg viewBox="0 0 12 12"><circle cx="6" cy="6" r="5" fill="none" stroke="var(--green)" stroke-width="1.2"/><ellipse cx="6" cy="6" rx="2" ry="5" fill="none" stroke="var(--green)" stroke-width="1"/><path d="M1 6 H11" stroke="var(--green)" stroke-width="1"/></svg>
      www.varnekelectrical.com.au
    </li>
  </ul>

  <address class="address">
    Varnek Electrical Service Pvt Ltd<br>
    PO Box 218<br>
    Linwood VA 20431
  </address>
</section>

<section class="card card--back" aria-label="Business card back">
  <svg class="card__art" viewBox="0 0 692 393" preserveAspectRatio="none" aria-hidden="true">
    <defs>
      <radialGradient id="navyBack" cx="0.45" cy="0.3" r="0.8">
        <stop offset="0" stop-color="#2c3d86"/>
        <stop offset="1" stop-color="var(--navy-deep)"/>
      </radialGradient>
      <linearGradient id="streak" x1="0" y1="0" x2="1" y2="0">
        <stop offset="0" stop-color="#ffffff" stop-opacity="0"/>
        <stop offset="0.7" stop-color="#ffffff" stop-opacity="0.18"/>
        <stop offset="1" stop-color="#ffffff" stop-opacity="0.05"/>
      </linearGradient>
    </defs>
    <rect width="692" height="393" fill="url(#navyBack)"/>
    <path d="M290 393 L470 0 L560 0 L360 393 Z" fill="url(#streak)"/>
  </svg>

  <div class="brand brand--back">
    <span class="brand__dot"></span>
    <span class="brand__name">Varnek Electrical<small>Services Pty Ltd</small></span>
  </div>

  <p class="tagline">For All Your Electrical Needs!</p>
</section>

</body>
</html>
```